PowerPoint template design for TLBavendish Consulting

I'm interested in a PowerPoint template design that incorporates my logo (see attached file). I am an economist who mostly shows charts and tables in Calibri 24 point. Most tables are 4 or 5 columns by 14 or 15 rows so the design should seek to maximize work space on the slide while unmistakably indicating that these are my slides. I will be using the template design when I provide copies of my slides to the audience after the presentation, mostly in PDF format.

Target Market(s)

Mostly non-data types including educators.

Industry/Entity Type

Consulting

Font styles to use
Sans Serif

Colors
00a990
33b8a4
86cfc6

Requirements
Must have
• Looking for something more sleek and subtle, that doesn't take up too much screen real estate and that in some manner incorporates my business card/logo design. The logo doesn't have to be exactly incorporated as is, but it should visually align or mesh. I like the teal and gray/dark gray color palette that is on my business card.
Nice to have
• Open to more transparency/faded coloring, less bold and vivid than subtle background.
Should not have
• The goal is a PP template design that is unmistakably mine but is not so intrusive that it is the focus of every slide. I want the viewer to forget that the slide is coming from me as a consultant and focus on the content of the slide. I'm not using this as part of a marketing or advertising push as much as I am marking my material so folks who refer to the slides at a later date will know that they are mine.

```html
<!DOCTYPE html>
<html lang="en">
<head>
<meta charset="utf-8">
<title>Texas Labor Market Themes of the Day – Slide Template</title>
<link rel="stylesheet" href="https://fonts.googleapis.com/css2?family=Carlito:wght@400;700&display=swap">
<style>
  :root {
    --teal: #00a990;
    --teal-mid: #33b8a4;
    --teal-soft: #86cfc6;
    --charcoal: #33383c;
    --charcoal-deep: #2a2e31;
    --gray-line: #d5d9db;
    --row-alt: #eef7f5;
    --ink: #3c4245;
    --white: #ffffff;
  }
  * { box-sizing: border-box; margin: 0; padding: 0; }
  html, body { width: 800px; height: 1200px; overflow: hidden; }
  body {
    background: var(--charcoal-deep);
    font-family: "Carlito", "Calibri", sans-serif;
    color: var(--ink);
  }
  .canvas {
    position: relative;
    width: 800px;
    height: 1200px;
    padding: 14px;
    display: flex;
    flex-direction: column;
    gap: 14px;
  }
  .slide {
    flex: 1;
    display: flex;
    flex-direction: column;
    background: var(--charcoal);
    border: 2px solid var(--teal-mid);
    padding: 8px;
    gap: 8px;
  }
  .theme-band {
    height: 50px;
    display: flex;
    align-items: center;
    justify-content: space-between;
    padding: 0 10px 0 18px;
    background: var(--charcoal-deep);
    border-bottom: 2px solid var(--teal);
  }
  .slide--footer .theme-band {
    border-bottom: none;
    border-top: 2px solid var(--teal);
  }
  .theme-title {
    color: var(--teal-soft);
    font-weight: 700;
    font-size: 20px;
    letter-spacing: 1.5px;
    text-transform: uppercase;
  }
  .brand {
    display: flex;
    align-items: center;
    gap: 6px;
    background: var(--white);
    padding: 6px 10px;
    height: 34px;
  }
  .brand-mark {
    width: 12px;
    height: 12px;
    background: var(--teal);
  }
  .brand-name {
    font-weight: 700;
    font-size: 15px;
    color: var(--charcoal);
    white-space: nowrap;
  }
  .work-area {
    flex: 1;
    background: var(--white);
    border: 1px solid var(--teal-soft);
    padding: 12px 14px;
    display: flex;
    flex-direction: column;
  }
  .table-title {
    background: var(--teal);
    color: var(--white);
    font-weight: 700;
    font-size: 19px;
    letter-spacing: 0.6px;
    text-transform: uppercase;
    padding: 7px 12px;
    margin-bottom: 6px;
  }
  .data-table {
    width: 100%;
    border-collapse: collapse;
    font-size: 14px;
  }
  .data-table th {
    text-align: left;
    font-weight: 700;
    padding: 5px 10px;
    border-bottom: 2px solid var(--teal);
  }
  .data-table td {
    padding: 0 10px;
    height: 26px;
    font-weight: 700;
    border-bottom: 1px solid var(--gray-line);
  }
  .data-table tbody tr:nth-child(even) td { background: var(--row-alt); }
  .col-major { width: 64%; }
  .col-grads { width: 16%; }
</style>
</head>
<body>
<main class="canvas">

  <section class="slide slide--header">
    <header class="theme-band">
      <span class="theme-title">Texas Labor Market Themes of the Day</span>
      <span class="brand"><span class="brand-mark"></span><span class="brand-name">TLBavendish Consulting</span></span>
    </header>
    <div class="work-area">
      <h2 class="table-title">Highest Earning Associate's Degree Programs 2014</h2>
      <table class="data-table">
        <thead>
          <tr><th class="col-major">Associate's Degree Graduate Major (TX) (50+)</th><th class="col-grads">Grads</th><th>Earnings</th></tr>
        </thead>
        <tbody>
          <tr><td>Fire Protection</td><td>197</td><td>$68,582</td></tr>
          <tr><td>Physical Science Technologies/Chemical Process</td><td>676</td><td>$59,074</td></tr>
          <tr><td>Quality Control and Safety Technologies/Techs</td><td>146</td><td>$58,246</td></tr>
          <tr><td>Electrical and Power Transmission Installers</td><td>56</td><td>$58,149</td></tr>
          <tr><td>Fire Protection</td><td>197</td><td>$68,582</td></tr>
          <tr><td>Physical Science Technologies/Chemical Process</td><td>676</td><td>$59,074</td></tr>
          <tr><td>Quality Control and Safety Technologies/Techs</td><td>146</td><td>$58,246</td></tr>
          <tr><td>Electrical and Power Transmission Installers</td><td>56</td><td>$58,149</td></tr>
          <tr><td>Fire Protection</td><td>197</td><td>$68,582</td></tr>
          <tr><td>Physical Science Technologies/Chemical Process</td><td>676</td><td>$59,074</td></tr>
          <tr><td>Quality Control and Safety Technologies/Techs</td><td>146</td><td>$58,246</td></tr>
          <tr><td>Electrical and Power Transmission Installers</td><td>56</td><td>$58,149</td></tr>
          <tr><td>Fire Protection</td><td>197</td><td>$68,582</td></tr>
          <tr><td>Electrical and Power Transmission Installers</td><td>56</td><td>$58,149</td></tr>
        </tbody>
      </table>
    </div>
  </section>

  <section class="slide slide--footer">
    <div class="work-area">
      <h2 class="table-title">Highest Earning Associate's Degree Programs 2014</h2>
      <table class="data-table">
        <thead>
          <tr><th class="col-major">Associate's Degree Graduate Major (TX) (50+)</th><th class="col-grads">Grads</th><th>Earnings</th></tr>
        </thead>
        <tbody>
          <tr><td>Fire Protection</td><td>197</td><td>$68,582</td></tr>
          <tr><td>Physical Science Technologies/Chemical Process</td><td>676</td><td>$59,074</td></tr>
          <tr><td>Quality Control and Safety Technologies/Techs</td><td>146</td><td>$58,246</td></tr>
          <tr><td>Electrical and Power Transmission Installers</td><td>56</td><td>$58,149</td></tr>
          <tr><td>Fire Protection</td><td>197</td><td>$68,582</td></tr>
          <tr><td>Physical Science Technologies/Chemical Process</td><td>676</td><td>$59,074</td></tr>
          <tr><td>Quality Control and Safety Technologies/Techs</td><td>146</td><td>$58,246</td></tr>
          <tr><td>Electrical and Power Transmission Installers</td><td>56</td><td>$58,149</td></tr>
          <tr><td>Fire Protection</td><td>197</td><td>$68,582</td></tr>
          <tr><td>Physical Science Technologies/Chemical Process</td><td>676</td><td>$59,074</td></tr>
          <tr><td>Quality Control and Safety Technologies/Techs</td><td>146</td><td>$58,246</td></tr>
          <tr><td>Electrical and Power Transmission Installers</td><td>56</td><td>$58,149</td></tr>
          <tr><td>Fire Protection</td><td>197</td><td>$68,582</td></tr>
          <tr><td>Electrical and Power Transmission Installers</td><td>56</td><td>$58,149</td></tr>
        </tbody>
      </table>
    </div>
    <footer class="theme-band">
      <span class="theme-title">Texas Labor Market Themes of the Day</span>
      <span class="brand"><span class="brand-mark"></span><span class="brand-name">TLBavendish Consulting</span></span>
    </footer>
  </section>

</main>
</body>
</html>
```